Bright Fern Painting needs a new business card. See attachments for our logo and current card as an example.
We want to utilize the same colors in the logo, and keep all the information that is currently on it. Just need an updated and modern design.
We are open to loosing the Association Logos if it means a better design.
We are also entertaining a spot for a picture of a headshot of the person listed on the card. Head shot can be finished later.

```html
<!DOCTYPE html>
<html lang="en">
<head>
<meta charset="utf-8">
<title>Bright Fern Painting – Business Card</title>
<link rel="stylesheet" href="https://fonts.googleapis.com/css2?family=PT+Sans:wght@400;700&family=Saira+Condensed:ital,wght@1,800&display=swap">
<style>
  :root {
    --olive: #3f4430;
    --maroon: #6e3b36;
    --ink: #3a3a36;
    --paper: #ffffff;
    --silver: #9a9c92;
    --backdrop: #3b2f2a;
  }
  * { margin: 0; padding: 0; box-sizing: border-box; }
  html, body { width: 1200px; height: 960px; overflow: hidden; }
  body {
    background: var(--backdrop);
    font-family: "PT Sans", sans-serif;
    position: relative;
  }
  .card {
    position: absolute;
    left: 250px;
    width: 700px;
    height: 400px;
    overflow: hidden;
    box-shadow: 0 10px 28px rgba(0,0,0,0.45);
  }
  /* Back of card */
  .card-back { top: 50px; background: var(--olive); }
  .card-back .brand {
    position: absolute;
    left: 48px; top: 72px;
    width: 230px;
    font-weight: 700;
    font-size: 38px;
    line-height: 1.05;
    color: var(--silver);
  }
  .services {
    position: absolute;
    left: 300px; top: 92px;
    list-style: none;
  }
  .services li {
    display: flex;
    align-items: center;
    gap: 12px;
    font-family: "Saira Condensed", sans-serif;
    font-style: italic;
    font-weight: 800;
    font-size: 34px;
    letter-spacing: 1px;
    line-height: 1.2;
    color: var(--paper);
    text-transform: uppercase;
  }
  .services svg { width: 28px; height: 28px; flex: none; }

  /* Front of card */
  .card-front { top: 510px; background: var(--paper); }
  .card-front .band { position: absolute; inset: 0; }
  .contact {
    position: absolute;
    left: 140px; top: 150px;
    color: var(--ink);
  }
  .contact .name {
    font-size: 38px;
    font-weight: 400;
    color: var(--maroon);
    text-transform: uppercase;
    letter-spacing: 0.5px;
    line-height: 1;
  }
  .contact .role {
    font-size: 15px;
    text-transform: uppercase;
    letter-spacing: 0.5px;
    margin-top: 4px;
    margin-bottom: 16px;
  }
  .contact .line { font-size: 18px; line-height: 1.3; }
  .card-front .brand {
    position: absolute;
    right: 48px; top: 130px;
    display: flex;
    align-items: center;
    gap: 14px;
    font-weight: 700;
    font-size: 34px;
    line-height: 1.05;
    color: var(--olive);
  }
  .card-front .brand .mark {
    width: 22px; height: 22px;
    background: var(--maroon);
    flex: none;
  }
</style>
</head>
<body>

<section class="card card-back">
  <div class="brand">Bright Fern Painting</div>
  <ul class="services">
    <li><svg viewBox="0 0 28 28" aria-hidden="true"><rect x="2" y="5" width="21" height="21" fill="none" stroke="#fff" stroke-width="2"/><path d="M7 15 L12 21 L26 2" fill="none" stroke="#fff" stroke-width="2.5"/></svg>Exterior Painting</li>
    <li><svg viewBox="0 0 28 28" aria-hidden="true"><rect x="2" y="5" width="21" height="21" fill="none" stroke="#fff" stroke-width="2"/><path d="M7 15 L12 21 L26 2" fill="none" stroke="#fff" stroke-width="2.5"/></svg>Interior Painting</li>
    <li><svg viewBox="0 0 28 28" aria-hidden="true"><rect x="2" y="5" width="21" height="21" fill="none" stroke="#fff" stroke-width="2"/><path d="M7 15 L12 21 L26 2" fill="none" stroke="#fff" stroke-width="2.5"/></svg>Carpentry</li>
    <li><svg viewBox="0 0 28 28" aria-hidden="true"><rect x="2" y="5" width="21" height="21" fill="none" stroke="#fff" stroke-width="2"/><path d="M7 15 L12 21 L26 2" fill="none" stroke="#fff" stroke-width="2.5"/></svg>Drywall</li>
  </ul>
</section>

<section class="card card-front">
  <svg class="band" viewBox="0 0 700 400" aria-hidden="true">
    <path d="M40 0 H112 V300 Q112 320 132 320 H700 V352 H40 Z" fill="var(--olive)"/>
  </svg>
  <div class="contact">
    <div class="name">Daniel Harper</div>
    <div class="role">Quality Manager</div>
    <div class="line">262-555-0148</div>
    <div class="line">daniel@brightfernpainting.com</div>
    <div class="line">brightfernpainting.com</div>
  </div>
  <div class="brand">
    <span class="mark"></span>
    <span>Bright Fern<br>Painting</span>
  </div>
</section>

</body>
</html>
```